Business Telephone Service Brochure

I need a brochure designed to help sell our VoIP service. The brochure needs to be clean, attention getting, professional and have 3 key areas of information (Key Features, Benefits & Service Plans). Here is an idea of what we are looking for https://www.plenvora.com/design/24930587. Need to also include how much the customer could save. See this for an example https://quarbeline.com/postcard-flyer-design/contests/voip-sales-flyer-template-replicate-attached-582913. The Service Plan section needs to allow room for two types of plans. One plan includes the phone and has a 12, 24 and 36 month option. Each term (12,24,36) will have its own monthly cost per device. The second service option is no-commitment monthly with a single per month price per device. The included features section should allow for up to 16 features to be listed. The benefits should allow for 4-6 benefits to be listed. Also include room for Logo, business address, website, phone number and email.

Target Market(s)

Small to medium business with 1-100 employees.

Industry/Entity Type

Telecommunications

Font styles to use
Serif

Colors

Designer to choose colors to be used in the design.

Requirements
Must have
• Key Feature, Benefits and Service Plans (i.e. Pricing). Company logo, phone, email and website. Must have "Save up to x%!" and catch attention.
Nice to have
• Limited colors. I am not setting a hard limit, please take the liberty to do what you feel is needed. Just keep in mind we want it to be clean, professional and attention getting without being to flashy or obnoxious.
Should not have
• Nothing busy or distracting.

```html
<!DOCTYPE html>
<html lang="en">
<head>
<meta charset="utf-8">
<title>Corvanet Business Phone Service Brochure</title>
<link rel="stylesheet" href="https://fonts.googleapis.com/css2?family=Anton&family=Open+Sans:wght@400;600;700&display=swap">
<style>
  :root {
    --bg: #d6d6d6;
    --ink-dark: #2e3033;
    --orange: #ef7d1e;
    --blue: #1a73c2;
    --sky: #2fb7e8;
    --green: #1f9a48;
    --navy: #1e2a78;
    --white: #ffffff;
    --muted: #c9ccd1;
  }
  * { margin: 0; padding: 0; box-sizing: border-box; }
  html, body { width: 1200px; height: 862px; overflow: hidden; }
  body {
    background: var(--bg);
    font-family: "Open Sans", Arial, sans-serif;
    color: var(--white);
    position: relative;
  }
  .page {
    position: absolute;
    top: 49px;
    width: 540px;
    height: 764px;
    background: var(--ink-dark);
    overflow: hidden;
    box-shadow: 0 6px 18px rgba(0,0,0,.25);
  }
  .page--back { left: 40px; }
  .page--front { left: 620px; }
  .page svg.shapes { position: absolute; inset: 0; }
  .photo-area { position: absolute; }

  /* Front */
  .brand {
    position: absolute; top: 24px; right: 22px;
    width: 196px; height: 74px;
    background: var(--white); border-radius: 10px;
    display: flex; align-items: center; justify-content: center; gap: 10px;
  }
  .brand__mark { width: 16px; height: 16px; background: var(--navy); }
  .brand__name { font-weight: 700; font-size: 34px; color: var(--navy); letter-spacing: -0.5px; }
  .save {
    position: absolute; left: 28px; top: 536px; margin: 0;
    color: var(--orange); font-family: "Anton", Impact, sans-serif; line-height: 0.95;
  }
  .save__big { font-size: 58px; display: block; }
  .save__small { font-size: 24px; display: block; }
  .plans {
    position: absolute; left: 28px; top: 624px; width: 484px;
    border-collapse: collapse; font-size: 12px; text-align: center;
  }
  .plans th { background: var(--orange); font-weight: 600; padding: 6px 4px; line-height: 1.2; border: 1px solid var(--ink-dark); }
  .plans td { background: var(--blue); font-weight: 700; font-size: 13px; padding: 0 4px; height: 30px; border: 1px solid var(--ink-dark); }
  .plans td.plans__service { background: var(--green); text-align: left; font-weight: 400; font-size: 10.5px; padding: 3px 8px; line-height: 1.25; }
  .footnote { position: absolute; left: 28px; top: 733px; width: 484px; font-size: 8px; line-height: 1.4; color: var(--muted); }

  /* Back */
  .block-title { font-weight: 700; font-size: 17px; margin-bottom: 6px; }
  .bullets { list-style: none; font-size: 11.5px; line-height: 1.5; }
  .bullets li::before { content: "•"; margin-right: 6px; }
  .benefits { position: absolute; left: 300px; top: 128px; width: 222px; }
  .features { position: absolute; left: 24px; top: 300px; width: 290px; }
  .device { position: absolute; right: 40px; top: 560px; width: 130px; height: 66px; border-radius: 6px; }
  .device-caption { position: absolute; right: 40px; top: 634px; width: 150px; font-size: 9px; color: var(--muted); line-height: 1.4; }
  .contact {
    position: absolute; left: 24px; bottom: 16px; width: 492px;
    font-size: 10.5px; line-height: 1.55; color: var(--white);
  }
  .contact__name { font-weight: 700; font-size: 13px; color: var(--orange); }
</style>
</head>
<body>

  <!-- Back side: features, benefits and contact -->
  <section class="page page--back">
    <svg class="shapes" width="540" height="764" viewBox="0 0 540 764" aria-hidden="true">
      <polygon points="0,250 540,250 540,764 0,764" fill="#2e3033"/>
      <polygon points="0,270 420,170 430,560 0,670" fill="#ef7d1e"/>
      <polygon points="280,100 540,100 540,440 290,480" fill="#1a73c2"/>
    </svg>
    <div class="photo-area" role="img" aria-label="Photo of a businessman holding a tablet with glowing network graphics"
         style="left:0;top:0;width:540px;height:100px;background:linear-gradient(120deg,#2b3b52,#6f93ad 60%,#c9dbe6);"></div>
    <div class="photo-area" role="img" aria-label="Photo continuation"
         style="left:0;top:100px;width:280px;height:170px;background:linear-gradient(160deg,#4f6d86,#9bb8cb);clip-path:polygon(0 0,100% 0,100% 40%,0 100%);"></div>

    <div class="benefits">
      <h2 class="block-title">Benefits</h2>
      <ul class="bullets">
        <li>No expensive onsite hardware and equipment</li>
        <li>Easily scale up or down</li>
        <li>Free installation</li>
        <li>Lower monthly costs</li>
        <li>Increase reliability</li>
        <li>Easy self-administration</li>
      </ul>
    </div>

    <div class="features">
      <h2 class="block-title">Key Features</h2>
      <ul class="bullets">
        <li>Unlimited local and long distance calling</li>
        <li>HD Voice</li>
        <li>Business SMS/Text Messaging</li>
        <li>Personal and Shared Voicemail</li>
        <li>Audio Conferencing</li>
        <li>Intercom</li>
        <li>Mobile App</li>
        <li>Auto Attendant/Interactive Voice Routing</li>
        <li>Fax to web or email</li>
        <li>Web admin portal</li>
        <li>Music On Hold – Customizable</li>
        <li>Simultaneous ring / follow-me</li>
        <li>Redundancy/Failover – Never miss a call</li>
      </ul>
    </div>

    <div class="device" role="img" aria-label="Photo of a desk IP phone with colour screen"
         style="background:linear-gradient(180deg,#4a4d52,#17181a);"></div>
    <p class="device-caption">Halvex T230 desk phone included with term plans</p>

    <address class="contact" style="font-style:normal;">
      <span class="contact__name">Corvanet</span><br>
      410 Linden Park Road, Suite 200, Marlow Bay, CA 90000<br>
      (555) 014-2290 &nbsp;|&nbsp; sales@corvanet.example &nbsp;|&nbsp; www.corvanet.example
    </address>
  </section>

  <!-- Front side: offer and service plans -->
  <section class="page page--front">
    <div class="photo-area" role="img" aria-label="Photo of a smiling call centre agent with headset working in a bright office"
         style="left:0;top:0;width:540px;height:470px;background:linear-gradient(135deg,#eef2f5,#b7c6d2 55%,#7e8f9c);"></div>
    <svg class="shapes" width="540" height="764" viewBox="0 0 540 764" aria-hidden="true">
      <polygon points="430,330 540,290 540,345" fill="#1f9a48"/>
      <polygon points="0,440 540,300 540,380 0,520" fill="#ef7d1e"/>
      <polygon points="0,500 300,425 310,450 0,530" fill="#2fb7e8"/>
      <polygon points="0,530 310,450 540,380 540,764 0,764" fill="#2e3033"/>
    </svg>
    <div class="brand">
      <span class="brand__mark"></span>
      <span class="brand__name">Corvanet</span>
    </div>

    <p class="save"><span class="save__big">Save</span><span class="save__small">up to 50%!</span></p>

    <table class="plans">
      <thead>
        <tr>
          <th style="width:160px">Service</th>
          <th>Monthly</th>
          <th>12 Month<br>Term</th>
          <th>24 Month<br>Term</th>
          <th>36 Month<br>Term</th>
        </tr>
      </thead>
      <tbody>
        <tr>
          <td class="plans__service">* Phone service only<br>(phone sold separately)</td>
          <td>$21.95</td><td></td><td></td><td></td>
        </tr>
        <tr>
          <td class="plans__service">Service + ** Halvex<br>T230 Phone</td>
          <td></td><td>$24.95</td><td>$22.95</td><td>$20.95</td>
        </tr>
      </tbody>
    </table>

    <p class="footnote">* For monthly service you may purchase the Halvex T230 phone for $65 each, less taxes and shipping.<br>
      ** Halvex T230 phones are rented and due upon cancellation. Customer pays return shipping.</p>
  </section>

</body>
</html>
```